Brackenlow Rotors Business Card

We are a new company based in Central Queensland, Australia that uses specalised drones (Vantorq Sprayhawk K40) to undertake mainly agricultural operations, like spraying weeds, spraying crops, spreading seed etc. I have attached a Plimsy proof of a card I was thinking along the lines of - purely a start point. The drone used in the business card MUST be a Vantorq Sprayhawk K40.
I am very open to other ideas, especially fonts and layout. I don't have website etc set up yet.
The images are stock and easily interchangeable, I just ask that any background images reflect the local central Queensland area. The photo of the drone is not even complete (propellers cut off) and I need a new stock photo – I’m not sure if this is an issue, or I can pay for an image if need be. PLEASE FIND AN SPRAYHAWK K40 image - 4 sprayers, not 6.
The logo/business name is very draft and looking for further ideas, ideally incorporating drones or agriculture design elements into the design of the business name. The business name needs work on the graphic/design – it is a draft that I have included, the drone propellers (being a different colour) are DRAFT only and intended for changes. PLEASE DO NOT USE THE DRONE PORPELLER I HAVE USED AS A DRAFT. TRY TO FIND SOMETHING ELSE.. The arrow is a shape and not aligned in any way, I would also like ideas on different fonts and additional elements, like air streams, aviation elements, aviation or country western (farming like) themes and fonts etc.
Ideally looking at staying within the blue, green and yellow colours, keeping with an natural, outdoorsy, environmental feel.

Target Market(s)

Farmers, Agriculture, Local Governments, Land Managers

Industry/Entity Type

Agriculture, Drones, Aviation

Contact Information for Business Card

Agricultural Drone (Vantorq Sprayhawk K40), Farming, Business Name.

Font styles to use
Sans Serif

Colors
0054AA
0677BA
7BADD7
CADEEF
E8F1F8
0094D4
00A9DD
6FCCEA
C7EBF8
E9F6FB
00AB8E
00BBA5
67D7C9
C6EFE9
E9F9F6
59FF00
82FF00
B8FF75
E3FFCB
F4FFEA

Requirements
Must have
• Vantorq Sprayhawk K40 Drone
Should not have
• Tractors

```html
<!DOCTYPE html>
<html lang="en">
<head>
<meta charset="utf-8">
<title>Brackenlow Rotors Business Card</title>
<link rel="stylesheet" href="https://fonts.googleapis.com/css2?family=Montserrat:wght@400;500;600;700;800&display=swap">
<style>
  :root {
    --backdrop: #979797;
    --card: #ffffff;
    --green: #22ad5c;
    --green-soft: #55c987;
    --navy: #172a5a;
    --icon: #0f3b5f;
    --rule: #a9a9a9;
  }
  * { margin: 0; padding: 0; box-sizing: border-box; }
  html, body { width: 1172px; height: 1200px; overflow: hidden; background: var(--backdrop); }
  body { position: relative; font-family: "Montserrat", Arial, sans-serif; color: var(--navy); }

  .card {
    position: absolute;
    width: 1050px; height: 600px;
    background: var(--card);
    transform-origin: 0 0;
    transform: scale(0.8044);
    box-shadow: 0 3px 6px rgba(0,0,0,.35);
    overflow: hidden;
  }
  .card--front { left: 186px; top: 75px; }
  .card--back { left: 176px; top: 606px; }
  .card svg.shapes { position: absolute; left: 0; top: 0; }

  /* front */
  .brand-name {
    position: absolute; right: 53px; top: 150px;
    text-align: right;
    font-weight: 800; color: var(--green);
    font-size: 66px; line-height: 0.98; letter-spacing: -1px;
  }
  .services {
    position: absolute; left: 512px; top: 340px;
    display: flex; align-items: center;
  }
  .service {
    display: flex; align-items: flex-start; gap: 8px;
    font-size: 25px; line-height: 25px; color: var(--navy);
    padding: 0 12px 0 0;
  }
  .service + .service { border-left: 2px solid var(--navy); padding-left: 18px; }
  .service svg { margin-top: 6px; flex: none; }
  .front-web {
    position: absolute; right: 58px; top: 503px;
    white-space: nowrap; text-align: right;
    font-size: 33px; font-weight: 500; letter-spacing: 2px; color: var(--navy);
  }

  /* back */
  .back-brand {
    position: absolute; left: 57px; top: 80px;
    font-weight: 800; color: var(--green);
    font-size: 64px; line-height: 0.98; letter-spacing: -1px;
  }
  .person { position: absolute; left: 56px; top: 272px; }
  .person-name { font-size: 58px; font-weight: 700; line-height: 1; }
  .person-name .first { color: var(--green); }
  .person-name .last { color: var(--navy); }
  .person-role { font-size: 42px; font-weight: 400; margin-top: 6px; color: var(--navy); }
  .divider { position: absolute; left: 57px; top: 398px; width: 899px; height: 2px; background: var(--rule); }
  .contact {
    position: absolute; display: flex; align-items: center; gap: 14px;
    font-size: 25px; color: var(--navy); white-space: nowrap;
  }
  .contact .icon {
    width: 44px; height: 44px; border-radius: 50%;
    background: var(--icon); display: flex; align-items: center; justify-content: center; flex: none;
  }
  .contact--phone { left: 56px; top: 425px; }
  .contact--mail { left: 56px; top: 496px; }
  .contact--address { left: 564px; top: 424px; }
  .contact--web { left: 564px; top: 494px; }
</style>
</head>
<body>

<section class="card card--front">
  <svg class="shapes" width="1050" height="600" viewBox="0 0 1050 600">
    <defs>
      <linearGradient id="fieldPhoto" x1="0" y1="0" x2="0" y2="1">
        <stop offset="0" stop-color="#b9d6ef"/>
        <stop offset="0.3" stop-color="#cfe2ef"/>
        <stop offset="0.38" stop-color="#4c6a5a"/>
        <stop offset="0.55" stop-color="#7fa35a"/>
        <stop offset="0.82" stop-color="#5f7f3e"/>
        <stop offset="1" stop-color="#8aaa4a"/>
      </linearGradient>
    </defs>
    <polygon role="img" aria-label="Photo of a Vantorq Sprayhawk K40 spray drone flying over Central Queensland crop fields"
      points="0,0 440,0 462,300 572,500 488,600 0,600" fill="url(#fieldPhoto)"/>
    <g stroke="#ffffff" stroke-width="12" fill="none">
      <line x1="60" y1="40" x2="270" y2="250"/>
      <line x1="270" y1="250" x2="450" y2="75"/>
      <line x1="0" y1="430" x2="180" y2="610"/>
      <line x1="100" y1="520" x2="340" y2="280"/>
    </g>
    <polygon points="0,0 62,0 86,52 20,140 0,140" fill="var(--green-soft)"/>
    <polygon points="367,88 452,0 498,0 570,78 468,187" fill="var(--green-soft)" stroke="#fff" stroke-width="2" stroke-linejoin="round"/>
  </svg>

  <div class="brand-name">Brackenlow<br>Rotors</div>

  <div class="services">
    <div class="service">
      <svg width="17" height="17" viewBox="0 0 17 17"><circle cx="8.5" cy="8.5" r="8.5" fill="var(--navy)"/><path d="M4.5 8.8l2.6 2.5 5-5" stroke="#fff" stroke-width="2" fill="none"/></svg>
      <span>Spraying<br>weeds</span>
    </div>
    <div class="service">
      <svg width="17" height="17" viewBox="0 0 17 17"><circle cx="8.5" cy="8.5" r="8.5" fill="var(--navy)"/><path d="M4.5 8.8l2.6 2.5 5-5" stroke="#fff" stroke-width="2" fill="none"/></svg>
      <span>Spraying<br>weeds</span>
    </div>
    <div class="service">
      <svg width="17" height="17" viewBox="0 0 17 17"><circle cx="8.5" cy="8.5" r="8.5" fill="var(--navy)"/><path d="M4.5 8.8l2.6 2.5 5-5" stroke="#fff" stroke-width="2" fill="none"/></svg>
      <span>Spraying<br>weeds</span>
    </div>
  </div>

  <div class="front-web">www.brackenlow.com</div>
</section>

<section class="card card--back">
  <svg class="shapes" width="1050" height="600" viewBox="0 0 1050 600">
    <defs>
      <linearGradient id="faintLandscape" x1="0" y1="0" x2="0" y2="1">
        <stop offset="0" stop-color="#ffffff"/>
        <stop offset="0.4" stop-color="#f4f6f5"/>
        <stop offset="0.7" stop-color="#eef1ee"/>
        <stop offset="1" stop-color="#f3f5f1"/>
      </linearGradient>
    </defs>
    <rect role="img" aria-label="Faded photo of Central Queensland farmland and hills" width="1050" height="600" fill="url(#faintLandscape)"/>
    <polygon points="594,0 1050,0 1050,152 920,286 902,286" fill="var(--green)" stroke="var(--green)" stroke-width="8" stroke-linejoin="round"/>
    <polygon points="930,308 1050,180 1050,428" fill="var(--navy)" stroke="var(--navy)" stroke-width="6" stroke-linejoin="round"/>
  </svg>

  <div class="back-brand">Brackenlow<br>Rotors</div>

  <div class="person">
    <div class="person-name"><span class="first">Darren</span> <span class="last">Kellow</span></div>
    <div class="person-role">Founder</div>
  </div>
  <div class="divider"></div>

  <div class="contact contact--phone">
    <span class="icon"><svg width="24" height="24" viewBox="0 0 24 24"><path d="M6.6 3.5l3 3-2 2.4c1.2 2.6 3.2 4.6 5.6 5.7l2.4-2 3 3-2.2 2.6C10.6 18.5 5.5 13.4 4 6.3z" fill="#fff"/></svg></span>
    <span>555-014-2290</span>
  </div>
  <div class="contact contact--mail">
    <span class="icon"><svg width="24" height="24" viewBox="0 0 24 24"><rect x="3" y="6" width="18" height="12" fill="none" stroke="#fff" stroke-width="1.8"/><path d="M3 6l9 7 9-7M3 18l7-6M21 18l-7-6" fill="none" stroke="#fff" stroke-width="1.5"/></svg></span>
    <span>darren@brackenlowmail.com</span>
  </div>
  <div class="contact contact--address">
    <span class="icon"><svg width="24" height="24" viewBox="0 0 24 24"><path d="M12 2.5c-3.8 0-6.5 2.8-6.5 6.4 0 4.6 6.5 12.6 6.5 12.6s6.5-8 6.5-12.6c0-3.6-2.7-6.4-6.5-6.4z" fill="#fff"/><circle cx="12" cy="9" r="2.6" fill="var(--icon)"/></svg></span>
    <span>27 Wattle Street Emerald,QLD</span>
  </div>
  <div class="contact contact--web">
    <span class="icon"><svg width="26" height="26" viewBox="0 0 26 26"><g fill="none" stroke="#fff" stroke-width="1.6"><circle cx="13" cy="13" r="9"/><ellipse cx="13" cy="13" rx="4" ry="9"/><line x1="4" y1="13" x2="22" y2="13"/><line x1="5.5" y1="8.5" x2="20.5" y2="8.5"/><line x1="5.5" y1="17.5" x2="20.5" y2="17.5"/></g></svg></span>
    <span>www.brackenlowrotors.com</span>
  </div>
</section>

</body>
</html>
```